Name of company is Raven Crest Shear Sharpening and Sales.Card design basic idea; I'm thinking back side just showing a sharp RAVEN CREST. Front side: I'm thinking a tiger showing teeth and claws.With the words "Raven Crest" larger type emphasized on one line.Then "Shear Sharpening and Sales" on the next line.Other info on front of card should be my name and phone #'s and address: Martin Kessling P (555)014-2287 CP (555)017-3365 My address is NOT to be emphasized.Can go at bottom of card. It is: 5072 Henley Court Orlando FL 30417 If all that's too much to fit without looking cluttered than maybe the claw on the front with all the contact info. and just the Tiger on back of card. Whichever looks best.

Target Market(s)

Beauty Salons

Industry/Entity Type

It Company

Contact Information for Business Card

The 2 images,the claw and the tiger,could be either illustrations or photos.Whatever looks best.Got to be eye grabbing either way.

Requirements
Must have
• Contact info. Must be in color. And emphasize the identity. RAVEN CREST.Tiger on one side.Showing TEETH. Raven Crest on the other side. Showing the CLAW. .Both pics must emphasize SHARPNESS...This is a shear SHARPENING business. If one of the claw pics shows cutting grooves into something that's fine too. Card must show sharpness of the claw blade somehow.
Nice to have
• Attention grabbing. Images should jump off the card!
Should not have
• No boring cuddly tiger pics showing no teeth or claws or dull teeth or claws. No Black and whites.. No extra words other than what I've listed.

```html
<!DOCTYPE html>
<html lang="en">
<head>
<meta charset="utf-8">
<title>Raven Crest – Business Card</title>
<link rel="stylesheet" href="https://fonts.googleapis.com/css2?family=Fjalla+One&family=Open+Sans:wght@300;400&display=swap">
<style>
  :root {
    --page-bg: #d9d6d2;
    --card-bg: #f3f1ee;
    --ink-dark: #353535;
    --brand-orange: #f3921e;
    --text-light: #ffffff;
  }
  * { margin: 0; padding: 0; box-sizing: border-box; }
  html, body {
    width: 1200px;
    height: 900px;
    overflow: hidden;
    background: var(--page-bg);
  }
  .business-card {
    position: absolute;
    left: 111px;
    top: 148px;
    width: 978px;
    height: 603px;
    background: var(--card-bg);
    overflow: hidden;
    box-shadow: 0 10px 30px rgba(0,0,0,0.18);
  }
  .card-shapes {
    position: absolute;
    inset: 0;
    width: 100%;
    height: 100%;
  }
  .shape-accent { fill: var(--brand-orange); }
  .shape-panel { fill: var(--ink-dark); }

  .brand-name {
    position: absolute;
    left: 54px;
    top: 248px;
    font-family: "Fjalla One", sans-serif;
    font-size: 74px;
    line-height: 1;
    letter-spacing: 1px;
    color: var(--ink-dark);
    white-space: nowrap;
  }
  .brand-tagline {
    position: absolute;
    left: 56px;
    top: 331px;
    font-family: "Open Sans", sans-serif;
    font-weight: 400;
    font-size: 26px;
    line-height: 1;
    color: var(--brand-orange);
    white-space: nowrap;
  }
  .owner-name {
    position: absolute;
    left: 54px;
    top: 452px;
    font-family: "Fjalla One", sans-serif;
    font-size: 46px;
    line-height: 1;
    letter-spacing: 2px;
    color: var(--brand-orange);
    white-space: nowrap;
  }
  .contact-phones,
  .contact-address {
    position: absolute;
    right: 42px;
    font-family: "Open Sans", sans-serif;
    font-weight: 400;
    font-size: 25px;
    line-height: 35px;
    color: var(--text-light);
    text-align: right;
    white-space: nowrap;
  }
  .contact-phones { top: 305px; }
  .contact-address { top: 458px; }
  .phone-line {
    display: flex;
    align-items: center;
    justify-content: flex-end;
    gap: 8px;
  }
  .phone-icon {
    width: 18px;
    height: 20px;
    fill: var(--text-light);
  }
</style>
</head>
<body>
  <main class="business-card">
    <svg class="card-shapes" viewBox="0 0 652 402" preserveAspectRatio="none" aria-hidden="true">
      <polygon class="shape-accent" points="652,0 640,0 448,80 505,118 350,272 418,262 200,402 652,402"/>
      <polygon class="shape-panel" points="652,6 462,84 522,118 364,268 434,258 222,402 652,402"/>
    </svg>

    <h1 class="brand-name">RAVEN CREST</h1>
    <p class="brand-tagline">SHEAR SHARPENING AND SALES</p>

    <p class="owner-name">MARTIN KESSLING</p>

    <div class="contact-phones">
      <p class="phone-line">(555)014-2287
        <svg class="phone-icon" viewBox="0 0 24 24" aria-label="phone" role="img">
          <path d="M6.6 10.8a15.1 15.1 0 0 0 6.6 6.6l2.2-2.2a1 1 0 0 1 1-.25 11.4 11.4 0 0 0 3.6.57 1 1 0 0 1 1 1V20a1 1 0 0 1-1 1A17 17 0 0 1 3 4a1 1 0 0 1 1-1h3.5a1 1 0 0 1 1 1c0 1.25.2 2.45.57 3.57a1 1 0 0 1-.25 1z"/>
        </svg>
      </p>
      <p class="phone-line">(555)017-3365
        <svg class="phone-icon" viewBox="0 0 24 24" aria-label="mobile phone" role="img">
          <path d="M7 1h10a2 2 0 0 1 2 2v18a2 2 0 0 1-2 2H7a2 2 0 0 1-2-2V3a2 2 0 0 1 2-2zm0 3v14h10V4zm5 15.5a1 1 0 1 0 0 2 1 1 0 0 0 0-2z"/>
        </svg>
      </p>
    </div>

    <address class="contact-address" style="font-style:normal">
      <p>5072 Henley Court</p>
      <p>Orlando FL 30417</p>
    </address>
  </main>
</body>
</html>
```